I need a business card design for my new clinic (ATHLETIC CARE OF JOINT). I am orthopedist, expert in sports surgery, especially knee surgery. I prefer, as colors, the colors of my logo (green, black and white). I already have my logo and should appear on my card. It's good to see my site to have ideas (www.drlucianovarela.example)
It needs contain:
my name: Dr. Luciano Varela
my registration: CRM 584-902
my specialty: Cirurgia do Joelho / Esporte
my address: Centro Empresarial - Parque Aurora Mall
Av. Doutor Augusto Valadares Pinto, 2740 sala 803
Jd. Acácias - Ribeirão Preto - SP
my phone number: Tel (16) 8420-5937
my clinic phone: (16) 3745-8081
my e-mail: drlucianovarela@mailbox.example
my site: www.drlucianovarela.example

Target Market(s)

futures patients

Industry/Entity Type

Clinic

Requirements
Nice to have
• letters not overfilled
straight lines, with few curves

```html
<!DOCTYPE html>
<html lang="pt-BR">
<head>
<meta charset="utf-8">
<title>Business Card – Dr. Luciano Varela</title>
<link href="https://fonts.googleapis.com/css2?family=Tinos:wght@400;700&display=swap" rel="stylesheet">
<style>
  :root {
    --page-bg: #e9e4dc;
    --card-dark-top: #2b2b2b;
    --card-dark-bottom: #0b0b0b;
    --card-light: #ffffff;
    --brand-green: #4cbf85;
    --text-light: #ffffff;
    --text-soft: #d8d8d8;
    --text-dark: #111111;
  }
  * { margin: 0; padding: 0; box-sizing: border-box; }
  html, body {
    width: 1200px; height: 1000px; overflow: hidden;
    background: var(--page-bg);
    font-family: "Tinos", "Times New Roman", serif;
  }
  .canvas { position: relative; width: 1200px; height: 1000px; }
  .card {
    position: absolute; left: 303px; width: 594px; height: 350px; overflow: hidden;
    box-shadow: 0 6px 14px rgba(0,0,0,0.25);
  }
  .card--front { top: 136px; background: linear-gradient(160deg, var(--card-dark-top), var(--card-dark-bottom) 70%); }
  .card--back { top: 513px; background: var(--card-light); }
  .card__wave { position: absolute; inset: 0; width: 594px; height: 350px; }

  .brand { position: absolute; display: flex; align-items: center; gap: 12px; }
  .brand__mark { width: 56px; height: 54px; border: 2px solid var(--text-light); border-radius: 6px; background: var(--brand-green); }
  .brand__name { color: var(--text-light); font-size: 44px; font-weight: 400; letter-spacing: 0.5px; line-height: 1; }
  .card--front .brand { left: 184px; top: 148px; }
  .card--back .brand { left: 30px; top: 40px; }

  .website {
    position: absolute; left: 0; right: 0; top: 300px; text-align: center;
    color: var(--text-light); font-size: 17px;
  }

  .doctor { position: absolute; right: 34px; top: 30px; text-align: right; color: var(--text-light); }
  .doctor__name { font-size: 21px; font-weight: 700; }
  .doctor__crm { font-size: 17px; font-weight: 700; margin-top: 6px; }
  .doctor__specialty { font-size: 13px; color: var(--text-soft); margin-top: 10px; }
  .doctor__mobile { font-size: 13px; color: var(--text-soft); margin-top: 5px; }

  .contact { position: absolute; left: 20px; top: 228px; color: var(--text-dark); font-size: 11.5px; font-weight: 700; line-height: 13.6px; }
  .contact__phone { margin-top: 10px; }
  .contact__email { margin-top: 9px; }
</style>
</head>
<body>
<main class="canvas">
  <section class="card card--front">
    <div class="brand">
      <span class="brand__mark"></span>
      <span class="brand__name">VARELA</span>
    </div>
    <p class="website">www.drlucianovarela.example</p>
  </section>

  <section class="card card--back">
    <svg class="card__wave" viewBox="0 0 594 350" aria-hidden="true">
      <defs>
        <linearGradient id="darkFill" x1="0" y1="0" x2="1" y2="1">
          <stop offset="0" stop-color="#2b2b2b"/>
          <stop offset="0.7" stop-color="#0b0b0b"/>
        </linearGradient>
      </defs>
      <path d="M0,0 H594 V236 C520,258 420,268 330,252 C230,232 120,166 0,162 Z" fill="url(#darkFill)"/>
      <path d="M0,165 C120,169 230,235 330,255 C420,271 520,261 594,239" fill="none" stroke="var(--brand-green)" stroke-width="6"/>
    </svg>
    <div class="brand">
      <span class="brand__mark"></span>
      <span class="brand__name">VARELA</span>
    </div>
    <div class="doctor">
      <p class="doctor__name">Dr. Luciano Varela</p>
      <p class="doctor__crm">CRM 584-902</p>
      <p class="doctor__specialty">Cirurgia do Joelho / Esporte</p>
      <p class="doctor__mobile">(16) 8420-5937</p>
    </div>
    <div class="contact">
      <p class="contact__address">Centro Empresarial - Parque Aurora Mall<br>Av. Doutor Augusto Valadares Pinto,<br>2740 sala 803, Jd. Acácias<br>Ribeirão Preto - SP</p>
      <p class="contact__phone">(16) 3745-8081</p>
      <p class="contact__email">drlucianovarela@mailbox.example</p>
    </div>
  </section>
</main>
</body>
</html>
```